Young Balance Support Network

We need a poster explaining that some children live with a disability called Vestibular Disorder. Feel free to ask question. We want you to respect our color code, same as our logo.

Here is our website : http://www.ybsnetwork.org/

We need to sensibilise people about this disability for children.

Industry/Entity Type

Charity

Font styles to use
Serif

Requirements
Must have
• 1. our logo (with all our details) + one of the photo of Marek
• 2. design showing a child with a dizziness for exemple
• 3. a title saying : Aidez-nous à changer la vie des enfants vivant avec un problème vestibulaire
• 4.include the text attached (information flyer YBSN)
• Poster size : 24"X 36"
Should not have
• wheel chair

```html
<!DOCTYPE html>
<html lang="fr">
<head>
<meta charset="utf-8">
<title>Young Balance Support Network – Affiche</title>
<link href="https://fonts.googleapis.com/css2?family=Courier+Prime:wght@400;700&display=swap" rel="stylesheet">
<style>
  :root {
    --teal-deep: #1f9aa0;
    --teal: #3db3b6;
    --teal-light: #8fd3d2;
    --mist: #eef7f6;
    --ink: #1d2d2f;
    --heading: #123a3e;
    --paper: #f7f5f0;
    --photo-dark: #6b5a48;
    --photo-light: #d9ccb8;
    --white: #ffffff;
  }
  * { margin: 0; padding: 0; box-sizing: border-box; }
  html, body { width: 800px; height: 1200px; overflow: hidden; }
  body {
    font-family: "Courier Prime", "Courier New", monospace;
    color: var(--ink);
    background: linear-gradient(180deg,
      var(--teal) 0px,
      var(--teal-light) 380px,
      var(--mist) 500px,
      var(--teal) 560px,
      var(--teal-light) 620px,
      var(--mist) 700px,
      var(--mist) 880px,
      var(--teal-light) 1050px,
      var(--teal-deep) 1200px);
    position: relative;
  }
  .hero-frame {
    position: absolute;
    left: 172px; top: 14px;
    width: 456px; height: 488px;
    background: var(--paper);
    padding: 18px 18px 40px;
    transform: rotate(-2.5deg);
    box-shadow: 0 6px 14px rgba(0,0,0,0.35);
  }
  .hero-photo {
    width: 100%; height: 100%;
    background: radial-gradient(ellipse at 55% 50%, var(--photo-light) 0%, #b8a68c 55%, var(--photo-dark) 100%);
  }
  .poster-title {
    position: absolute;
    top: 542px; left: 30px; width: 740px;
    text-align: center;
    color: var(--white);
    font-weight: 700;
    font-size: 25px;
    line-height: 31px;
    text-transform: uppercase;
    text-shadow: 2px 2px 3px rgba(0,0,0,0.55);
  }
  .info {
    position: absolute;
    top: 624px; left: 58px; width: 712px;
  }
  .info h2 {
    font-size: 20px;
    line-height: 24px;
    font-weight: 700;
    color: var(--heading);
    margin-top: 28px;
    margin-bottom: 3px;
  }
  .info h2:first-child { margin-top: 0; }
  .info p {
    font-size: 14px;
    line-height: 18px;
    margin-bottom: 14px;
  }
  .info p:last-child { margin-bottom: 0; }
</style>
</head>
<body>
  <div class="hero-frame">
    <div class="hero-photo" role="img" aria-label="Photo sépia d'un jeune enfant portant des lunettes"></div>
  </div>

  <h1 class="poster-title">Aidez-nous à changer la vie des enfants<br>vivant avec un problème vestibulaire</h1>

  <main class="info">
    <h2>Qu'est-ce que le vestibule ?</h2>
    <p>C'est un organe essentiel, pilier de votre équilibre,<br>véritable 6ème sens situé dans l'oreille interne.</p>

    <h2>Qu'est ce qu'une aréflexie vestibulaire ?</h2>
    <p>C'est l'absence complète de toute information vestibulaire.<br>L'enfant a ainsi l'impression que tout vacille autour de lui, jour et nuit.</p>

    <h2>Quelles en sont les conséquences pour l'enfant ?</h2>
    <p>Le développement moteur de l'enfant est retardé car il doit trouver des solutions afin de construire son équilibre, stabiliser son regard et son corps.</p>
    <p>Certains apprentissages sont de véritables obstacles pour l'enfant : se représenter son propre corps, se situer dans l'espace qui l'entoure, interagir avec les autres, communiquer, écrire, lire, manger, boire, marcher. Chacune de ces actions nécessitent des efforts considérables pour se concentrer quelques secondes ou minutes.</p>
    <p>Quand l'enfant réussit à effectuer l'une de ces actions, son comportement peut sembler déroutant et bien trop souvent mal interprété par le grand public.</p>

    <h2>Quel est le but de notre association ?</h2>
    <p>Notre association a pour but de promouvoir les troubles vestibulaires chez l'enfant, ses conséquences sur sa santé ainsi que celle de son entourage et de soutenir ces enfants et leurs parents en leur offrant un espace de parole et des solutions concrètes pour soulager leur quotidien. Notre association a également pour but de financer et promouvoir toute action de recherche scientifique visant à aider les enfants ayant un trouble vestibulaire.</p>
  </main>
</body>
</html>
```